Kitchen and Bathroom Remodeling Flyer

This flyer is for a home remodeling company that remodels peoples kitchens and bathrooms.

We want a flyer to be sophisticated: nice professional design with classy font.

FRONT OF FLYER:

I have attached the front flyer I created and there is no design to it. The reason is so you can see what text elements we want on the flyer. a second attachment has the text for easy copy and paste.

I like the idea of mentioning “Owners live in Ahwatukee” because this flyer will be passed around door to door in that town of Ahwatukee.

Please use the image and the corresponding headline specific to that image. The headline can be in the image or to the top of the image.

BACK OF FLYER:
The back of flyer is essentially a written letter with a profile image of our owners and then two testimonials at bottom. I’d like to add a little bit of design to the back of the flyer. See attachment for pdf of current text and basic structure.

Our brand colors are gray and blue# 0000cc

Our website is https://Kelmbrookrenovating.com

Thank you,
Tobias

Target Market(s)

Mostly woman. Homeowners making 100k+ a year that want to remodel their kitchen or bathroom

Industry/Entity Type

Home Improvement

Font styles to use
Serif
Sans Serif
Decorative

Colors

Designer to choose colors to be used in the design.

Requirements
Must have
• This has to be in photoshop with each element editable (I’ll want to change things down the road)
Nice to have
• Examples that I don’t want copied but so you have a rough idea of some design structure that I like:
• https://flyer.pixelvantyard.com/contest.aspx?id=5190362
• https://flyer.pixelvantyard.com/contest.aspx?id=627053
• https://flyer.pixelvantyard.com/contest.aspx?id=8831475
• https://www.pixelvantyard.com/design/42957018
• https://www.pixelvantyard.com/design/7160243
Should not have
• Nothing silly or too loud. Thank you

```html
<!DOCTYPE html>
<html lang="en">
<head>
<meta charset="utf-8">
<title>Kelmbrook Renovating Flyer</title>
<link rel="stylesheet" href="https://fonts.googleapis.com/css2?family=Questrial&family=Ubuntu:wght@400;500&family=Arimo:ital,wght@0,400;1,700&family=Yellowtail&display=swap">
<style>
:root{
  --stage:#231f20;
  --paper:#dcdcdc;
  --blue:#0c349b;
  --ink-blue:#1a3a9c;
  --gray-text:#6b6b6b;
  --dark:#2b2b2b;
  --white:#ffffff;
}
*{margin:0;padding:0;box-sizing:border-box}
html,body{width:1200px;height:1200px;overflow:hidden;background:var(--stage)}
.canvas{position:relative;width:1200px;height:1200px}
.page{position:absolute;background:var(--paper);overflow:hidden}
.abs{position:absolute}

/* front */
.front{left:63px;top:112px;width:516px;height:730px;font-family:"Ubuntu",sans-serif}
.site-url{right:24px;top:14px;font-size:10px;color:var(--ink-blue)}
.brand{left:36px;top:84px;display:flex;align-items:center;gap:6px}
.brand-mark{width:12px;height:12px;background:var(--blue)}
.brand-name{font-size:14px;color:var(--gray-text)}
.headline{left:262px;top:49px;font-family:"Questrial",sans-serif;color:var(--blue);line-height:.95}
.headline .small{font-size:20px;display:block}
.headline .big{font-size:41px;display:block;letter-spacing:.5px}
.top-band{left:0;top:134px;width:516px;height:22px;background:var(--blue)}
.kitchen-photo{left:0;top:156px;width:516px;height:274px;background:linear-gradient(180deg,#c9c9c6 0%,#eeeeec 35%,#f6f6f4 60%,#b9bbbd 100%)}
.caption{background:rgba(236,236,236,.86);color:var(--dark);line-height:1.15}
.caption .lead{font-size:10px;display:block}
.caption .key{font-size:17px;display:block}
.kitchen-caption{left:0;top:190px;width:315px;height:54px;padding:10px 0 0 77px}
.promises{left:0;top:434px;width:233px;height:238px;background:var(--blue);color:var(--white);font-family:"Arimo",sans-serif}
.promises h2{position:absolute;left:14px;top:32px;font-size:13px;font-weight:700;font-style:italic}
.promises ul{position:absolute;left:14px;top:52px;list-style:none;font-size:7px;line-height:13.6px}
.promises li::before{content:"• "}
.cta{left:15px;top:147px;width:200px;height:77px;background:var(--white);color:var(--blue);text-align:center;font-family:"Ubuntu",sans-serif;padding-top:12px;line-height:1}
.cta .call{font-size:16px;display:block}
.cta .phone{font-size:20px;display:block;margin-top:1px}
.cta .more{font-size:10px;display:block;margin-top:1px}
.bath-photo{left:237px;top:434px;width:279px;height:238px;background:linear-gradient(90deg,#8a8b8c 0%,#5f5853 30%,#6e655d 60%,#cfcfcd 100%)}
.bath-caption{left:277px;top:604px;width:239px;height:51px;padding:6px 0 0 16px}
.front-footer-left{left:20px;top:694px;font-size:10px;color:var(--ink-blue);line-height:1.25}
.front-footer-right{right:20px;top:702px;font-size:10px;color:var(--ink-blue)}

/* back */
.back{left:621px;top:358px;width:516px;height:730px}
.letter{left:33px;top:40px;width:450px;font-family:"Yellowtail",cursive;color:var(--blue)}
.letter h1{font-size:21px;font-weight:400;margin:0 0 8px 6px}
.letter p{font-size:10px;line-height:15px;margin-bottom:15px}
.owners-band{left:0;top:373px;width:516px;height:200px;background:var(--blue)}
.owners-photo{left:119px;top:9px;width:136px;height:181px;background:linear-gradient(180deg,#b9cde0 0%,#9fb2a4 45%,#6a7a5a 75%,#4a5540 100%)}
.owners-info{left:282px;top:69px;font-family:"Ubuntu",sans-serif;font-size:10px;line-height:12.2px;color:#c8d2ec}
.owners-info strong{font-family:"Arimo",sans-serif;font-style:italic;font-weight:700;color:#dde3f4}
.reviews{left:0;top:573px;width:516px;height:133px;font-family:"Ubuntu",sans-serif;color:var(--ink-blue)}
.reviews-divider{left:258px;top:0;width:3px;height:133px;background:var(--white)}
.review-photo{width:74px;height:75px;background:linear-gradient(180deg,#9a8d82 0%,#c8c4bd 50%,#6d6d6d 100%)}
.review-name{font-size:10px;white-space:nowrap}
.review-place{font-size:6px;font-family:"Arimo",sans-serif;font-style:italic}
.review-quote{font-size:7.6px;line-height:10.3px;width:118px}
.back-footer{left:0;top:706px;width:516px;height:24px;background:var(--white);text-align:center;font-family:"Ubuntu",sans-serif;font-size:9.6px;color:var(--ink-blue);line-height:24px}
</style>
</head>
<body>
<div class="canvas">

  <section class="page front">
    <div class="abs site-url">Kelmbrookrenovating.com</div>
    <div class="abs brand"><span class="brand-mark"></span><span class="brand-name">Kelmbrook Renovating</span></div>
    <div class="abs headline"><span class="small">OWNERS</span><span class="small">LIVE-IN</span><span class="big">AHWATUKEE</span></div>
    <div class="abs top-band"></div>
    <div class="abs kitchen-photo" role="img" aria-label="Bright white kitchen with marble island and glass-front cabinets"></div>
    <div class="abs caption kitchen-caption"><span class="lead">ENTERTAIN IN A KITCHEN</span><span class="lead">YOU'LL LOVE SHOWING OFF TO</span><span class="key">FRIENDS &amp; FAMILY</span></div>

    <div class="abs promises">
      <h2>OUR CLIENT PROMISES</h2>
      <ul>
        <li>Provide honest and straight forward advice</li>
        <li>Return calls and show up on time</li>
        <li>Employ professional, respectful and knowledgeable employees</li>
        <li>Respect your home and ensure we keep it clean</li>
        <li>Provide clear expectations of project timelines and pricing</li>
        <li>Create your dream living space with great attention to detail</li>
      </ul>
      <div class="abs cta"><span class="call">CALL</span><span class="phone">602-555-0147</span><span class="more">FOR MORE INFORMATION</span></div>
    </div>

    <div class="abs bath-photo" role="img" aria-label="Modern bathroom with dark wood double vanity and glass shower"></div>
    <div class="abs caption bath-caption"><span class="lead">TURN AN</span><span class="lead">OLD BATHROOM INTO YOUR OWN</span><span class="key">PERSONAL SPA</span></div>

    <div class="abs front-footer-left">Kelmbrook Renovating<br>602-555-0147 ROC# 408215</div>
    <div class="abs front-footer-right">LICENSED | BONDED | INSURED</div>
  </section>

  <section class="page back">
    <div class="abs letter">
      <h1>Dear Ahwatukee Homeowners,</h1>
      <p>Everyone wants a dream home they can be proud of. We all want to feel prosperous in life and our home is an extension of ourselves, our style and feeling successful.</p>
      <p>We understand working with a remodeling contractor can be frustrating because they show up late, change the price and make a mess of your home.</p>
      <p>Kelmbrook Renovating is the most organized remodeling company in the valley and we'll create the dream space you'll be proud to show off to your friends, family, &amp; neighbors.</p>
      <p>One of our co-founders Tobias has been through several contractor nightmares and it is the main reason Tobias, Russ and Declan founded Kelmbrook Renovating.</p>
      <p>We are an award-winning home remodeling licensed contractor that is known for showing up on time, being organized, clearly explaining all aspects of the remodel, adhering to project budget and timeline.</p>
      <p>One of our client's said we were the DriveLane of home remodeling and we think that's a nice comparison. We'll guide you through our 4 step process and there's no haggle, no sales BS and our clients love the experience.</p>
      <p>To a beautiful home you'll love showing off to your neighbors, family &amp; friends.</p>
    </div>

    <div class="abs owners-band">
      <div class="abs owners-photo" role="img" aria-label="The three co-owners standing outdoors with palm trees behind them"></div>
      <div class="abs owners-info"><strong>Tobias, Declan and Russ</strong><br>Kelmbrook Renovating<br>ROC# 408215<br>Kelmbrookrenovating.com<br>602-555-0147</div>
    </div>

    <div class="abs reviews">
      <div class="abs review-photo" style="left:23px;top:13px" role="img" aria-label="Portrait of a happy client couple"></div>
      <div class="abs review-name" style="left:23px;top:93px">Owen and Lila M.</div>
      <div class="abs review-place" style="left:23px;top:109px">Biltmore &nbsp;Phoenix, AZ</div>
      <div class="abs review-quote" style="left:123px;top:16px">“Our bathroom is amazing! The crew was polite,<br>easy to work with and they kept our house clean.<br><br>I always knew what was happening and there weren't any surprises. My wife and I are very happy. &nbsp;Thank you!”</div>

      <div class="abs reviews-divider"></div>

      <div class="abs review-photo" style="left:282px;top:16px" role="img" aria-label="Portrait of a smiling client couple"></div>
      <div class="abs review-name" style="left:282px;top:101px">Marisa &amp; Paul T.</div>
      <div class="abs review-place" style="left:282px;top:117px">Chandler, AZ</div>
      <div class="abs review-quote" style="left:390px;top:18px">“Declan and his team were easy to work<br>with and their attention to detail was great.<br><br>Our kitchen looks perfect just how we wanted it and we couldn't be happier. Thank you Kelmbrook Renovating.”</div>
    </div>

    <div class="abs back-footer">Kelmbrookrenovating.com</div>
  </section>

</div>
</body>
</html>
```